RETAIL/ONLINE sports store needing redesign of homepage

Sports store In need of a face lift for our website we have been in business the last several years and needs freshening up and modernising.

Please take note of the following:

Keep it clean and clutter free
Any colour to be considered
Rough and rugged theme but not essential, open to ideas
FB / twitter / intagram logo/links
Easy access to virtual store as we want to promote we are not just online
Use New logo, find attached
We have 2 parts to the business
75% retail
25% training
Easy navigation to the above section with miniuim scrolling down the page
Retail access needs to have more exposure than the training section
Address/contact details to both parts of the business needs to be easily seen as these are in 2 different locations
latest news section to be used
Any suggestion would be aprciated

For reference please visit our old website for ideas
www.k3gymworks.example

Target Market(s)

healthy life style, fitness fanatic, power lifting, olympic lifting, specialised fitness supplier

Industry/Entity Type

Retail

Number of Pages Required

1 page

Requirements
Must have
• logo
• contact details
• address
• link to virtual store
• social media links
• latest news section
Nice to have
• nice colours - easy navigation - access to virtual store - latest new section -
Should not have
• cluttered - hard to access the store -

```html
<!DOCTYPE html>
<html lang="en">
<head>
<meta charset="utf-8">
<title>K3 Gymworks – Home</title>
<link href="https://fonts.googleapis.com/css2?family=Open+Sans:ital,wght@0,400;0,600;0,700;1,600;1,700&display=swap" rel="stylesheet">
<style>
:root{
  --page:#e9ecee;
  --teal:#1d4d63;
  --teal-deep:#183f52;
  --slate:#222d33;
  --slate-2:#1b2429;
  --blue:#1d9ad6;
  --blue-box:#1292c9;
  --red:#ef5040;
  --white:#ffffff;
  --muted:#b5c2c9;
  --grey-text:#8fa0a8;
}
*{margin:0;padding:0;box-sizing:border-box}
html,body{width:1200px;height:1200px;overflow:hidden;background:var(--page);font-family:'Open Sans',sans-serif}
.site{position:absolute;left:0;top:115px;width:1113px;height:850px;background:linear-gradient(180deg,var(--teal) 0,var(--teal-deep) 317px,var(--slate) 317px,var(--slate-2) 100%);overflow:hidden}
.abs{position:absolute}
.brand{left:152px;top:22px;color:var(--blue);font-weight:700;font-size:27px;line-height:1;letter-spacing:1px;white-space:nowrap}
.brand small{display:block;font-size:11px;color:var(--white);letter-spacing:3px;margin-top:38px;font-weight:700;font-style:italic}
.hours{left:384px;top:23px;width:205px;text-align:center;color:var(--muted);font-size:12px;line-height:17px;white-space:nowrap}
.hours b{display:block;color:var(--blue);font-size:14px;font-weight:700;line-height:18px}
.cart{left:637px;top:16px;color:var(--white);font-size:10px;font-weight:600}
.cart .row{display:flex;align-items:center;gap:8px;margin-left:4px}
.cart .field{display:flex;margin-top:6px}
.cart .count{background:var(--white);color:var(--blue);font-size:9px;padding:3px 6px;width:105px;white-space:nowrap}
.cart .buy{background:var(--blue);color:var(--white);font-size:10px;font-weight:700;padding:2px 14px 3px 14px;width:50px}
.nav{left:357px;top:86px;display:flex;gap:22px}
.nav a{color:var(--white);text-decoration:none;font-style:italic;font-weight:600;font-size:13px;text-transform:uppercase}
.slider{left:136px;top:107px;width:658px;height:210px;background:linear-gradient(90deg,#1f5c7a 0,#4a5a63 30%,#7b7a78 55%,#b8b4ac 80%,#8e8c88 100%)}
.section-title{font-style:italic;font-weight:700;font-size:25px;color:var(--blue);line-height:1}
.section-title span{color:var(--muted)}
.address{display:flex;gap:5px;align-items:flex-start;color:var(--red);font-style:italic;font-weight:600;font-size:13px;line-height:16px;margin-top:8px}
.arrow-btn{width:24px;height:24px;border:2px solid var(--white);border-radius:50%;background:#1f6c90;display:flex;align-items:center;justify-content:center}
.social{left:589px;top:366px;display:flex;gap:7px}
.social i{width:21px;height:21px;border-radius:50%;background:#c9cfd2;display:block}
.photo{width:193px;height:118px;border:1px solid #3b4a52}
.ticks{list-style:none;color:var(--white);font-size:9.5px;line-height:16.6px}
.ticks li{display:flex;align-items:center;gap:8px}
.reserve{left:155px;top:608px;width:167px;height:27px;background:var(--red);display:flex;align-items:center;justify-content:center;gap:6px;color:#2a3a44;font-weight:700;font-size:13px}
.reserve i{width:16px;height:16px;border-radius:50%;background:#1f6c90;display:flex;align-items:center;justify-content:center}
.posts{left:584px;top:395px;width:198px;height:227px;background:var(--blue-box);padding:12px 10px 0 16px;color:var(--white)}
.posts h3{font-size:12.5px;font-weight:600;margin-bottom:12px}
.posts ul{list-style:none;font-size:9.5px;line-height:13px}
.posts li{display:flex;gap:7px;padding:5px 0 7px;border-bottom:1px dashed rgba(255,255,255,.55);width:174px}
.posts li:last-child{border:none}
.posts li::before{content:"";width:0;height:0;align-self:flex-start;border-left:6px solid var(--white);border-top:4px solid transparent;border-bottom:4px solid transparent;margin-top:2px;flex:none}
.posts .more{display:block;margin-top:12px;color:#173f52;font-weight:700;font-size:11px}
.foot h4{color:var(--white);font-size:12px;font-weight:600;margin-bottom:9px}
.links{list-style:none;color:var(--grey-text);font-size:9px;line-height:16px}
.contacts{color:var(--grey-text);font-size:10.5px;line-height:20px;font-weight:600}
.cards{display:flex;gap:5px}
.cards span{background:var(--white);color:#1a3b6b;font-weight:700;font-size:9px;width:52px;height:22px;display:flex;align-items:center;justify-content:center}
.foot-brand{left:358px;top:797px;color:#56666e;font-weight:700;font-size:16px;letter-spacing:2px}
.copy{left:365px;top:822px;color:#4d5d65;font-size:9px}
</style>
</head>
<body>
<div class="site">
  <header>
    <div class="abs brand">K3 GYMWORKS<small>FITNESS STORE</small></div>
    <div class="abs hours">Lines are open from 10 am to 18 pm<b>Monday to friday</b><b>(555)014-2290</b></div>
    <div class="abs cart">
      <div class="row">
        <svg width="24" height="16" viewBox="0 0 24 16"><path d="M1 2h4l3 9h11l3-7H7" fill="none" stroke="#fff" stroke-width="2"/><circle cx="10" cy="14" r="1.6" fill="#fff"/><circle cx="18" cy="14" r="1.6" fill="#fff"/></svg>
        Your shopping Cart
      </div>
      <div class="field"><span class="count">0 item(s) in your cart.</span><span class="buy">Buy</span></div>
    </div>
    <nav class="abs nav"><a>Home</a><a>Training</a><a>Store</a><a>Services</a><a>About us</a></nav>
  </header>

  <section class="abs slider" role="img" aria-label="Photo of the store interior with shelves of weights, supplements and training gear"></section>
  <div class="abs" style="left:152px;top:121px">
    <div class="section-title"><span>K3</span> STORE</div>
    <div class="address">
      <svg width="11" height="15" viewBox="0 0 11 15"><path d="M5.5 0a5.5 5.5 0 0 1 5.5 5.5C11 9.5 5.5 15 5.5 15S0 9.5 0 5.5A5.5 5.5 0 0 1 5.5 0z" fill="#ef5040"/><circle cx="5.5" cy="5.5" r="2" fill="#fff"/></svg>
      <span>Unit 5 Harrow Court,<br>Mill Street, Eastport 4</span>
    </div>
  </div>
  <div class="abs arrow-btn" style="left:145px;top:216px"><svg width="10" height="10" viewBox="0 0 10 10"><path d="M6.5 1.5 3 5l3.5 3.5" stroke="#fff" stroke-width="2" fill="none"/></svg></div>
  <div class="abs arrow-btn" style="left:757px;top:213px"><svg width="10" height="10" viewBox="0 0 10 10"><path d="M3.5 1.5 7 5 3.5 8.5" stroke="#fff" stroke-width="2" fill="none"/></svg></div>

  <section>
    <div class="abs" style="left:152px;top:336px">
      <div class="section-title"><span>K3</span> TRAINING</div>
      <div class="address">
        <svg width="11" height="15" viewBox="0 0 11 15"><path d="M5.5 0a5.5 5.5 0 0 1 5.5 5.5C11 9.5 5.5 15 5.5 15S0 9.5 0 5.5A5.5 5.5 0 0 1 5.5 0z" fill="#ef5040"/><circle cx="5.5" cy="5.5" r="2" fill="#fff"/></svg>
        <span>Fenwick House, 9 Quay Lane, Eastport 4</span>
      </div>
    </div>
    <div class="abs social" aria-label="Social network links"><i></i><i></i><i></i><i></i></div>

    <div class="abs photo" role="img" aria-label="Photo of the training gym with racks and weight plates" style="left:153px;top:397px;background:linear-gradient(135deg,#5b6a72,#2e3d66 45%,#3b4348)"></div>
    <div class="abs photo" role="img" aria-label="Photo of a trainer coaching a client lifting dumbbells" style="left:371px;top:397px;background:linear-gradient(135deg,#c9ccd0,#a7a4a3 45%,#8b5a5a 70%,#6d7a86)"></div>

    <ul class="abs ticks" style="left:157px;top:525px">
      <li><svg width="10" height="11" viewBox="0 0 10 11"><path d="M1 6l3 3 5-8" stroke="#ef5040" stroke-width="2.4" fill="none"/></svg>Body transformation camp</li>
      <li><svg width="10" height="11" viewBox="0 0 10 11"><path d="M1 6l3 3 5-8" stroke="#ef5040" stroke-width="2.4" fill="none"/></svg>Massage Therapist</li>
      <li><svg width="10" height="11" viewBox="0 0 10 11"><path d="M1 6l3 3 5-8" stroke="#ef5040" stroke-width="2.4" fill="none"/></svg>Transformation camp</li>
      <li><svg width="10" height="11" viewBox="0 0 10 11"><path d="M1 6l3 3 5-8" stroke="#ef5040" stroke-width="2.4" fill="none"/></svg>Kettlebell training</li>
    </ul>
    <ul class="abs ticks" style="left:375px;top:526px">
      <li><svg width="10" height="11" viewBox="0 0 10 11"><path d="M1 6l3 3 5-8" stroke="#ef5040" stroke-width="2.4" fill="none"/></svg>Body transformation camp</li>
      <li><svg width="10" height="11" viewBox="0 0 10 11"><path d="M1 6l3 3 5-8" stroke="#ef5040" stroke-width="2.4" fill="none"/></svg>Massage Therapist</li>
      <li><svg width="10" height="11" viewBox="0 0 10 11"><path d="M1 6l3 3 5-8" stroke="#ef5040" stroke-width="2.4" fill="none"/></svg>Transformation camp</li>
      <li><svg width="10" height="11" viewBox="0 0 10 11"><path d="M1 6l3 3 5-8" stroke="#ef5040" stroke-width="2.4" fill="none"/></svg>Kettlebell training</li>
    </ul>
    <div class="abs reserve"><i><svg width="8" height="8" viewBox="0 0 8 8"><path d="M2.5 1 5.5 4 2.5 7" stroke="#fff" stroke-width="1.6" fill="none"/></svg></i>Reservation</div>

    <aside class="abs posts">
      <h3>RECENT POSTS</h3>
      <ul>
        <li>Store Closed – July 30 – August 6</li>
        <li>Review: NovaLabs NX2<br>Rice Protein</li>
        <li>Riverside Strength Throwdown</li>
        <li>The perfomance base: your base<br>for becoming the best</li>
      </ul>
      <a class="more">Read more &gt;&gt;</a>
    </aside>
  </section>

  <footer>
    <div class="abs foot" style="left:146px;top:680px">
      <h4>WHY BUY FROM US ?</h4>
      <ul class="links" style="padding-left:9px">
        <li>&gt; Secure Online Payments</li><li>&gt; Terms &amp; Conditions</li><li>&gt; Privacy Policy</li><li>&gt; Returns Policy</li><li>&gt; Delivery &amp; Collection</li>
      </ul>
    </div>
    <div class="abs foot" style="left:354px;top:680px">
      <h4>CONTACTS INFOS</h4>
      <div class="contacts">(555) 014-2290<br>info@k3gymworks.example<br>www.k3gymworks.example</div>
    </div>
    <div class="abs foot" style="left:593px;top:680px">
      <h4>SECURE ONLINE PAIEMENTS</h4>
      <div class="cards"><span>PayCard</span><span>CardPlus</span><span>VoucherGo</span></div>
    </div>
    <div class="abs foot-brand">K3 GYMWORKS</div>
    <div class="abs copy">© Copyright 2015 - www.k3gymworks.example</div>
  </footer>
</div>
</body>
</html>
```